Roof wash and Gutter Cleaning

Would like to see our colors and logo incorporated into design along with phone number and before/after picture(s). We use a non pressure softwash process we use unlike high pressure. We are a exterior cleaning company that likes to set our standards high with safe methods to cleaning the everyday surfaces on homes.
“Serving the Tri-State Area”
A list of our services:
House washing
Shingle and metal roof washing
Deck cleaning
Window cleaning
Concrete cleaning
Gutter cleaning
514-362-0917
We do not need the address section as these will be more for our meet and greets. As well handed out as clipped door  postcards.

Shingle roof wash and gutter cleaning

```html
<!DOCTYPE html>
<html lang="en">
<head>
<meta charset="utf-8">
<title>Summit Exterior Cleaning – Postcard</title>
<link href="https://fonts.googleapis.com/css2?family=Oswald:wght@500;600&family=Montserrat:wght@600;700;800&family=Lato:ital,wght@1,400;1,700&display=swap" rel="stylesheet">
<style>
  :root {
    --stage: #333333;
    --white: #ffffff;
    --green: #3fa34d;
    --blue: #2d6ec8;
    --blue-deep: #1f56b0;
    --navy: #0f2350;
    --teal: #2f8d96;
    --star: #f6b21b;
    --tag-grey: #6b7a8a;
  }
  * { box-sizing: border-box; margin: 0; padding: 0; }
  html, body { width: 1200px; height: 1177px; overflow: hidden; background: var(--stage); }
  .card { position: absolute; left: 220px; width: 757px; background: var(--white); overflow: hidden; }
  .card--front { top: 64px; height: 503px; }
  .card--back { top: 605px; height: 507px; }
  .photo { position: absolute; }
  .service-label {
    position: absolute; color: var(--white);
    font: 700 17px/1.05 "Montserrat", sans-serif; text-transform: uppercase;
    display: flex; align-items: center; padding: 0 16px;
  }
  .service-label--green { background: var(--green); }
  .service-label--teal { background: var(--teal); }
  .service-label--blue { background: rgba(45,110,200,.85); }
  .front-art { position: absolute; inset: 0; }
  .brand { position: absolute; text-align: center; color: var(--blue); }
  .brand__name { display: inline-flex; align-items: center; gap: 8px; font: 800 50px/1 "Montserrat", sans-serif; }
  .brand__dot { width: 18px; height: 18px; border-radius: 50%; background: var(--green); }
  .brand__tag { font: 600 12px/1 "Montserrat", sans-serif; color: var(--tag-grey); margin-top: 14px; letter-spacing: .3px; }
  .front-brand { left: 240px; width: 277px; top: 92px; }
  .headline {
    position: absolute; left: 240px; width: 277px; top: 264px; text-align: center;
    color: var(--white); font: 600 42px/1.12 "Oswald", sans-serif; text-transform: uppercase;
  }
  .cta { position: absolute; left: 200px; width: 357px; top: 400px; text-align: center; color: var(--white); }
  .cta__lead { display: flex; align-items: center; justify-content: center; gap: 12px; font: 600 27px/1 "Montserrat", sans-serif; }
  .cta__lead::before, .cta__lead::after { content: ""; width: 44px; height: 2px; background: var(--white); }
  .cta__phone { font: 600 50px/1 "Oswald", sans-serif; margin-top: 10px; }
  .back-brand { left: 30px; top: 22px; width: 220px; }
  .back-brand .brand__name { font-size: 42px; }
  .back-brand .brand__tag { font-size: 10px; margin-top: 10px; }
  .back-phone { position: absolute; left: 24px; top: 124px; color: var(--navy); font: 600 42px/1 "Oswald", sans-serif; }
  .accreditation { position: absolute; left: 26px; top: 181px; width: 78px; height: 27px; border-radius: 3px; background: var(--teal); }
  .review-band { position: absolute; inset: 0; }
  .stars { position: absolute; left: 0; width: 757px; top: 212px; display: flex; justify-content: center; }
  .review {
    position: absolute; left: 0; width: 757px; top: 254px; text-align: center; color: var(--white);
    font: italic 400 16.5px/1.35 "Lato", sans-serif;
  }
  .review strong { font-weight: 700; }
  .comparison { position: absolute; top: 340px; width: 108px; }
  .comparison__frame { height: 123px; background: var(--white); border-radius: 6px; }
  .comparison__label {
    margin-top: 5px; height: 24px; display: flex; align-items: center; justify-content: center;
    color: var(--white); font: 700 13.5px/1 "Montserrat", sans-serif;
  }
  .comparison__label--after { background: var(--navy); border-radius: 0 0 5px 5px; margin-top: 0; height: 29px; padding-top: 4px; }
</style>
</head>
<body>

<section class="card card--front" aria-label="Postcard front">
  <div class="photo" role="img" aria-label="Worker soft-washing a house wall" style="left:0;top:0;width:260px;height:132px;background:linear-gradient(135deg,#8fa28a,#e2e2dc);"></div>
  <div class="service-label service-label--green" style="left:0;top:132px;width:260px;height:30px;">House washing</div>
  <div class="photo" role="img" aria-label="Worker washing a metal roof" style="left:0;top:162px;width:270px;height:174px;background:linear-gradient(135deg,#9aa3a8,#4b5358);"></div>
  <div class="service-label service-label--teal" style="left:0;top:296px;width:270px;height:40px;">Shingle and metal<br>roof washing</div>
  <div class="photo" role="img" aria-label="Pressure wand cleaning a wooden deck" style="left:0;top:336px;width:260px;height:167px;background:linear-gradient(135deg,#7a5634,#c29566);"></div>
  <div class="service-label service-label--blue" style="left:0;top:464px;width:200px;height:39px;">Deck<br>cleaning</div>

  <div class="photo" role="img" aria-label="Crew cleaning office building windows" style="left:497px;top:0;width:260px;height:132px;background:linear-gradient(135deg,#5d6266,#c9cccf);"></div>
  <div class="service-label service-label--green" style="left:497px;top:132px;width:260px;height:30px;justify-content:flex-end;">Window cleaning</div>
  <div class="photo" role="img" aria-label="Workers cleaning a concrete floor" style="left:487px;top:162px;width:270px;height:174px;background:linear-gradient(135deg,#e8e8e6,#a9aaa6);"></div>
  <div class="service-label service-label--teal" style="left:487px;top:296px;width:270px;height:40px;justify-content:flex-end;">Concrete cleaning</div>
  <div class="photo" role="img" aria-label="Worker on a ladder cleaning gutters" style="left:497px;top:336px;width:260px;height:167px;background:linear-gradient(135deg,#e6e4df,#7e8a6d);"></div>
  <div class="service-label service-label--blue" style="left:557px;top:464px;width:200px;height:39px;justify-content:flex-end;text-align:right;">Gutter<br>cleaning</div>

  <svg class="front-art" width="757" height="503" viewBox="0 0 757 503" aria-hidden="true">
    <defs>
      <clipPath id="center-panel">
        <path d="M210 0 C250 150 260 380 140 503 L617 503 C497 380 507 150 547 0 Z"/>
      </clipPath>
      <linearGradient id="cta-fill" x1="0" y1="0" x2="1" y2="0">
        <stop offset="0" stop-color="#2f6fd0"/>
        <stop offset=".5" stop-color="#1f56b0"/>
        <stop offset="1" stop-color="#2f6fd0"/>
      </linearGradient>
    </defs>
    <g clip-path="url(#center-panel)">
      <rect x="0" y="0" width="757" height="234" fill="#ffffff"/>
      <rect x="0" y="234" width="757" height="152" fill="#0f2350"/>
      <rect x="0" y="386" width="757" height="117" fill="url(#cta-fill)"/>
    </g>
    <path d="M210 0 C250 150 260 380 140 503" fill="none" stroke="#3fa34d" stroke-width="8"/>
    <path d="M547 0 C507 150 497 380 617 503" fill="none" stroke="#3fa34d" stroke-width="8"/>
    <path d="M218 0 C258 150 268 380 148 503" fill="none" stroke="#ffffff" stroke-width="3"/>
    <path d="M539 0 C499 150 489 380 609 503" fill="none" stroke="#ffffff" stroke-width="3"/>
  </svg>

  <div class="brand front-brand">
    <div class="brand__name"><span class="brand__dot"></span>Summit</div>
    <div class="brand__tag">Exterior Cleaning &amp; Maintenance Co.</div>
  </div>
  <h1 class="headline">Serving the<br>Tri-State Area</h1>
  <div class="cta">
    <div class="cta__lead">Call Us Now</div>
    <div class="cta__phone">514-362-0917</div>
  </div>
</section>

<section class="card card--back" aria-label="Postcard back">
  <div class="photo" role="img" aria-label="Greyscale photo of a worker cleaning a gutter" style="left:300px;top:0;width:457px;height:320px;background:linear-gradient(120deg,#ffffff 0%,#e4e5e6 35%,#bfc1c3 100%);"></div>

  <div class="brand back-brand">
    <div class="brand__name"><span class="brand__dot"></span>Summit</div>
    <div class="brand__tag">Exterior Cleaning &amp; Maintenance Co.</div>
  </div>
  <div class="back-phone">514-362-0917</div>
  <div class="accreditation" aria-hidden="true"></div>

  <svg class="review-band" width="757" height="507" viewBox="0 0 757 507" aria-hidden="true">
    <defs>
      <linearGradient id="review-fill" x1="0" y1="0" x2="1" y2="0">
        <stop offset="0" stop-color="#2d6ec8"/>
        <stop offset=".5" stop-color="#2f8d96"/>
        <stop offset="1" stop-color="#3fa34d"/>
      </linearGradient>
    </defs>
    <path d="M0 318 Q380 30 757 230 L757 507 L0 507 Z" fill="url(#review-fill)"/>
  </svg>

  <div class="stars" aria-label="Five star rating">
    <svg width="150" height="28" viewBox="0 0 150 28" aria-hidden="true">
      <g fill="#f6b21b" stroke="#c47d0a" stroke-width="1">
        <polygon points="14,1 17.8,9.6 27,10.4 20,16.6 22,25.8 14,21 6,25.8 8,16.6 1,10.4 10.2,9.6"/>
        <polygon transform="translate(30 0)" points="14,1 17.8,9.6 27,10.4 20,16.6 22,25.8 14,21 6,25.8 8,16.6 1,10.4 10.2,9.6"/>
        <polygon transform="translate(60 0)" points="14,1 17.8,9.6 27,10.4 20,16.6 22,25.8 14,21 6,25.8 8,16.6 1,10.4 10.2,9.6"/>
        <polygon transform="translate(90 0)" points="14,1 17.8,9.6 27,10.4 20,16.6 22,25.8 14,21 6,25.8 8,16.6 1,10.4 10.2,9.6"/>
        <polygon transform="translate(120 0)" points="14,1 17.8,9.6 27,10.4 20,16.6 22,25.8 14,21 6,25.8 8,16.6 1,10.4 10.2,9.6"/>
      </g>
    </svg>
  </div>
  <p class="review">Great work, cabin and roof look brand new after cleaning.<br>Prices are good work is excellent punctual and very friendly individuals.<br>I can't be happier! <strong>-MARGO L</strong></p>

  <div class="comparison" style="left:23px;"><div class="comparison__frame"></div><div class="comparison__label">BEFORE</div></div>
  <div class="comparison" style="left:140px;"><div class="comparison__frame"></div><div class="comparison__label comparison__label--after">AFTER</div></div>
  <div class="comparison" style="left:267px;"><div class="comparison__frame"></div><div class="comparison__label">BEFORE</div></div>
  <div class="comparison" style="left:385px;"><div class="comparison__frame"></div><div class="comparison__label comparison__label--after">AFTER</div></div>
  <div class="comparison" style="left:510px;"><div class="comparison__frame"></div><div class="comparison__label">BEFORE</div></div>
  <div class="comparison" style="left:629px;"><div class="comparison__frame"></div><div class="comparison__label comparison__label--after">AFTER</div></div>
</section>

</body>
</html>
```